Design letterhead , business card , email signature and envelope

Task:
We require letterhead , business card , email signature and envelope for Lumora Vitality. Logo files and info is attached.

----------
Company Background:
Lumora Vitality is a medical company which provides holistic alternative solutions using the latest cutting edge technology of genetic testing and other new equipment to avoid medication but get the patient well. the idea is not to follow the regular medical prescriptions for medicines, but rather keep people healthy through what they eat and what vitamins their bodies lack.

```html
<!DOCTYPE html>
<html lang="en">
<head>
<meta charset="utf-8">
<title>Lumora Vitality Stationery</title>
<link href="https://fonts.googleapis.com/css2?family=Poppins:wght@400;500;600;700&display=swap" rel="stylesheet">
<style>
:root{
  --bg:#2c2e31;
  --paper:#ffffff;
  --red:#e8262c;
  --green:#3cb54a;
  --ink:#333333;
  --muted:#6b6b6b;
  --photo:#e9e9ea;
  --faint:#f6dcd8;
}
*{margin:0;padding:0;box-sizing:border-box}
html,body{width:1200px;height:631px;overflow:hidden;background:var(--bg);font-family:"Poppins",sans-serif;color:var(--ink)}
.canvas{position:relative;width:1200px;height:631px}
.piece{position:absolute;background:var(--paper);overflow:hidden}
.brand{display:flex;align-items:center;gap:4px;font-weight:700;color:var(--red);letter-spacing:.04em;white-space:nowrap;text-transform:uppercase}
.brand .dot{border-radius:50%;background:var(--green);flex:none}
.contact{list-style:none;font-size:5.6px;line-height:1.5;color:var(--ink)}
.contact li{display:flex;align-items:flex-start;gap:4px}
.icon{flex:none;fill:var(--green)}
.lbl-g{color:var(--green)}
.lbl-r{color:var(--red)}

/* business card front */
.card-front{left:80px;top:50px;width:202px;height:114px;display:flex;flex-direction:column;align-items:center;justify-content:center}
.card-front .brand{font-size:10px;margin-top:8px}
.card-front .brand .dot{width:9px;height:9px}
.card-front .web{position:absolute;bottom:10px;left:0;right:0;display:flex;justify-content:center;gap:4px;font-size:5px}

/* business card back */
.card-back{left:80px;top:172px;width:202px;height:116px}
.card-back .person{position:absolute;right:8px;top:46px;text-align:right}
.card-back .name{font-size:9px;font-weight:600;color:var(--ink)}
.card-back .name b{color:var(--red);font-weight:600}
.card-back .role{font-size:6.5px;font-weight:500}
.card-back .rule{position:absolute;left:0;top:66px;width:130px;height:1px;background:var(--red)}
.card-back .contact{position:absolute;left:8px;top:68px;font-size:5px}

/* compliment slip */
.slip{left:298px;top:48px;width:288px;height:134px}
.slip .brand{position:absolute;left:20px;top:14px;font-size:6px}
.slip .brand .dot{width:6px;height:6px}
.slip .contact{position:absolute;left:18px;top:82px}
.slip .mark{position:absolute;left:190px;top:34px;width:62px;height:62px;border-radius:50%;background:var(--faint)}
.slip .wordmark{position:absolute;right:14px;top:106px;font-size:11px;font-weight:600;color:#f4b3a6;letter-spacing:.04em;text-transform:uppercase}

/* envelope */
.envelope{left:298px;top:190px;width:288px;height:136px}
.envelope .flap{position:absolute;left:0;top:0;width:288px;height:42px;background:var(--green);border-radius:0 0 14px 14px}
.envelope .brand{position:absolute;left:0;right:0;top:80px;justify-content:center;font-size:8px}
.envelope .brand .dot{width:8px;height:8px}

/* letterhead */
.letterhead{left:604px;top:55px;width:258px;height:316px;padding:18px 16px}
.letterhead .brand{position:absolute;left:14px;top:30px;font-size:5.4px}
.letterhead .brand .dot{width:5px;height:5px}
.letterhead .phones{position:absolute;right:12px;top:24px;font-size:4.6px;line-height:1.5}
.letterhead .to{position:absolute;left:14px;top:74px;font-size:4.4px;line-height:1.45}
.letterhead .to strong{color:var(--red);font-weight:600;font-size:5px}
.letterhead .date{position:absolute;right:14px;top:92px;font-size:5px;font-weight:500}
.letterhead .body{position:absolute;left:14px;right:14px;top:115px;font-size:3.8px;line-height:1.55;color:var(--muted)}
.letterhead .body p{margin-bottom:5px}
.letterhead .sign{position:absolute;left:14px;top:258px;font-size:4.4px;line-height:1.5}
.letterhead .mark{position:absolute;left:110px;top:160px;width:110px;height:110px;border-radius:50%;background:var(--faint);opacity:.6}
.letterhead .foot{position:absolute;right:12px;bottom:10px;display:flex;gap:4px;align-items:flex-start}
.letterhead .foot .lines{font-size:4px;line-height:2;text-align:right}
.letterhead .foot .icons{display:flex;flex-direction:column;gap:2px}
.chip{width:9px;height:9px;border-radius:50%;background:var(--green)}

/* email signature */
.signature{left:83px;top:351px;width:458px;height:90px}
.signature .photo{position:absolute;left:16px;top:11px;width:68px;height:68px;border-radius:50%;background:var(--photo);display:flex;align-items:center;justify-content:center;text-align:center;font-size:14px;line-height:1.05;color:var(--ink)}
.signature .person{position:absolute;left:110px;top:28px}
.signature .name{font-size:14px;font-weight:500}
.signature .name b{color:var(--red);font-weight:500}
.signature .role{font-size:13px;color:var(--muted);margin-left:16px}
.signature .bar{position:absolute;left:235px;top:20px;width:2px;height:52px;background:var(--red)}
.signature .contact{position:absolute;left:246px;top:20px;font-size:7px;line-height:1.55}
.signature .phones{position:absolute;left:244px;top:56px;font-size:7px;line-height:1.4}
.signature .addr{position:absolute;left:330px;top:56px;display:flex;gap:4px;font-size:7px;line-height:1.3}
.signature .mark{position:absolute;left:383px;top:20px;width:56px;height:56px;border-radius:50%;background:var(--faint);opacity:.7}
</style>
</head>
<body>
<main class="canvas">

  <section class="piece card-front" aria-label="Business card front">
    <div class="brand"><span class="dot"></span>Lumora Vitality</div>
    <div class="web"><svg class="icon" width="6" height="6" viewBox="0 0 10 10"><circle cx="5" cy="5" r="5"/></svg>www.lumoravitality.com</div>
  </section>

  <section class="piece card-back" aria-label="Business card back">
    <div class="person">
      <div class="name">Rina <b>Calloway</b></div>
      <div class="role">President</div>
    </div>
    <div class="rule"></div>
    <ul class="contact">
      <li><span class="lbl-r">Cell :</span> 201-5550142</li>
      <li><span class="lbl-g">Office:</span> 646-555-0187</li>
      <li><svg class="icon" width="6" height="6" viewBox="0 0 10 10"><circle cx="5" cy="5" r="5"/></svg>www.lumoravitality.com</li>
      <li><svg class="icon" width="6" height="6" viewBox="0 0 10 10"><rect x="0" y="2" width="10" height="7"/></svg>info@lumoravitality.com</li>
      <li><svg class="icon" width="6" height="7" viewBox="0 0 10 12"><path d="M5 0a4 4 0 0 1 4 4c0 3-4 8-4 8S1 7 1 4a4 4 0 0 1 4-4z"/></svg>48 Alder Lane, #210<br>Brookfield , NY 12000</li>
    </ul>
  </section>

  <section class="piece slip" aria-label="Compliment slip">
    <div class="brand"><span class="dot"></span>Lumora Vitality</div>
    <ul class="contact">
      <li><span class="lbl-g">Office:</span> 646-555-0187</li>
      <li><span class="lbl-r">Cell :</span> 201-5550142</li>
      <li><svg class="icon" width="6" height="6" viewBox="0 0 10 10"><circle cx="5" cy="5" r="5"/></svg>www.lumoravitality.com</li>
      <li><svg class="icon" width="6" height="6" viewBox="0 0 10 10"><rect x="0" y="2" width="10" height="7"/></svg>info@lumoravitality.com</li>
      <li><svg class="icon" width="6" height="7" viewBox="0 0 10 12"><path d="M5 0a4 4 0 0 1 4 4c0 3-4 8-4 8S1 7 1 4a4 4 0 0 1 4-4z"/></svg>48 Alder Lane, #210 ,<br>Brookfield , NY 12000</li>
    </ul>
    <div class="mark" aria-hidden="true"></div>
    <div class="wordmark">Lumora Vitality</div>
  </section>

  <section class="piece envelope" aria-label="Envelope">
    <div class="flap"></div>
    <div class="brand"><span class="dot"></span>Lumora Vitality</div>
  </section>

  <section class="piece letterhead" aria-label="Letterhead">
    <div class="brand"><span class="dot"></span>Lumora Vitality</div>
    <div class="phones"><span class="lbl-g">Office:</span> 646-555-0187<br><span class="lbl-r">Cell :</span> 201-5550142</div>
    <div class="to">TO,<br><strong>DANIEL PORTER</strong><br>MANAGER<br><br>48 Alder Lane, #210<br>Brookfield , NY 12000</div>
    <div class="date">DATE :23/02/2018</div>
    <div class="mark" aria-hidden="true"></div>
    <div class="body">
      <p>Thank you for choosing our clinic. This letter confirms your upcoming nutrition review and genetic screening appointment. Our team will study your results and prepare a personal plan covering diet, vitamins and daily habits that support lasting health without relying on routine medication.</p>
      <p>Please arrive fifteen minutes early and bring any recent lab reports.</p>
      <p>During the visit we will discuss your goals, food preferences and any symptoms you have noticed. A short sample will be collected for testing, and results usually return within two weeks. We will then schedule a follow up session to walk through each finding together.</p>
      <p>Feel free to contact our office with any questions before your appointment. We look forward to meeting you.</p>
    </div>
    <div class="sign">Rina Calloway<br>President</div>
    <div class="foot">
      <div class="lines">www.lumoravitality.com<br>info@lumoravitality.com<br>48 Alder Lane, #210<br>Brookfield , NY 12000</div>
      <div class="icons"><span class="chip"></span><span class="chip"></span><span class="chip"></span></div>
    </div>
  </section>

  <section class="piece signature" aria-label="Email signature">
    <div class="photo" role="img" aria-label="Portrait photo placeholder">your<br>photo</div>
    <div class="person">
      <div class="name">Rina <b>Calloway</b></div>
      <div class="role">President</div>
    </div>
    <div class="bar"></div>
    <ul class="contact">
      <li><svg class="icon" width="8" height="8" viewBox="0 0 10 10"><circle cx="5" cy="5" r="5"/></svg>www.lumoravitality.com</li>
      <li><svg class="icon" width="8" height="8" viewBox="0 0 10 10"><rect x="0" y="2" width="10" height="7"/></svg>info@lumoravitality.com</li>
    </ul>
    <div class="phones"><span class="lbl-r">Cell :</span> 201-5550142<br><span class="lbl-g">Office:</span> 646-555-0187</div>
    <div class="mark" aria-hidden="true"></div>
    <div class="addr"><svg class="icon" width="8" height="10" viewBox="0 0 10 12"><path d="M5 0a4 4 0 0 1 4 4c0 3-4 8-4 8S1 7 1 4a4 4 0 0 1 4-4z"/></svg><span>48 Alder Lane, #210<br>Brookfield , NY 12000</span></div>
  </section>

</main>
</body>
</html>
```